Self-Publisher seeking a professional Book Cover design

Paperback novel, science-fiction/mind-fiction. Title “Tovald’s Hollow”. Will be published via Pellow PBX and must meet their sizing requirements for a Book Cover (‘the spine”). (The book is 362 pages). The overall concept of design should be relatively simple, playing with themes of dark/blackness/space/unconscious/insanity-themes. Initially I had in mind a dark cover with something floating small and distant in the darkness like a sort of “space-cocoon”/hibernation-tank for an astronaut. (just something to get started thinking with). I am very open to any concepts.

From the back cover:
“In the year 3438, a discovery of a lifetime is made, and promises new light for a whole new generation of mankind which has permanently stagnated, becoming little more than slaves to their own technology which itself has already plateaued. Life goes on, yet for man, it stopped over a millennia ago. A secret project begun in the Ancient-American West in the year 1947, has catastrophic implications for the modern people’s of 3438. A discovery in space that lay apparently dormant for over a thousand years, mysteriously hidden from mankind’s ever evolving technological grasp, leads to a culture-shattering revelation that can only have one outcome. Chaos. …”

Target Market(s)

25-45 yr.

Industry/Entity Type

science-fiction, mind-bending, esotericism, psychological, space,

Font styles to use
Serif

Colors

Designer to choose colors to be used in the design.

Requirements
Must have
• darkness, with perhaps elements of bright light???
Should not have
• nothing too colorful. think, “unconscious”.

```html
<!DOCTYPE html>
<html lang="en">
<head>
<meta charset="utf-8">
<title>Tovald’s Hollow — Book Cover</title>
<link href="https://fonts.googleapis.com/css2?family=Cinzel:wght@400&display=swap" rel="stylesheet">
<style>
  :root {
    --page-bg: #ffffff;
    --cover-deep: #03080b;
    --cover-wall: #071419;
    --cover-mid: #0e3038;
    --cover-glow: #2a8a86;
    --cover-light: #9af5e2;
    --title-face: #eef6fd;
    --title-edge: #6a97d9;
    --author-ink: #e6eef1;
  }
  * { margin: 0; padding: 0; box-sizing: border-box; }
  html, body {
    width: 1200px;
    height: 1200px;
    overflow: hidden;
    background: var(--page-bg);
  }
  .canvas {
    position: relative;
    width: 1200px;
    height: 1200px;
    background: var(--page-bg);
  }
  .book-cover {
    position: absolute;
    left: 230px;
    top: 45px;
    width: 740px;
    height: 1111px;
    overflow: hidden;
    background: var(--cover-deep);
  }
  .cover-art {
    position: absolute;
    inset: 0;
    background:
      /* dark foreground ledge rising toward the right */
      linear-gradient(160deg, rgba(3,8,11,0) 0%, rgba(3,8,11,0) 66%, rgba(3,8,11,0.92) 72%, var(--cover-deep) 100%),
      linear-gradient(180deg, rgba(3,8,11,0) 0%, rgba(3,8,11,0) 70%, rgba(3,8,11,0.85) 80%, var(--cover-deep) 92%),
      /* cavern walls darkening the sides */
      linear-gradient(90deg, rgba(3,8,11,0.85) 0%, rgba(3,8,11,0) 22%, rgba(3,8,11,0) 78%, rgba(3,8,11,0.85) 100%),
      /* bright core of light behind the spires */
      radial-gradient(ellipse 22% 13% at 50% 64%, var(--cover-light) 0%, rgba(154,245,226,0.7) 40%, rgba(154,245,226,0) 100%),
      /* misty horizontal band */
      radial-gradient(ellipse 60% 9% at 48% 58%, rgba(120,220,205,0.45) 0%, rgba(120,220,205,0) 100%),
      /* wide teal haze */
      radial-gradient(ellipse 62% 36% at 50% 60%, var(--cover-glow) 0%, var(--cover-mid) 50%, rgba(14,48,56,0) 100%),
      linear-gradient(180deg, #05111a 0%, #0a2229 38%, #0c2a30 60%, var(--cover-wall) 78%, var(--cover-deep) 100%);
  }
  .cover-title {
    position: absolute;
    left: 0;
    right: 0;
    top: 118px;
    text-align: center;
    font-family: "Cinzel", "Trajan Pro", serif;
    font-weight: 400;
    font-size: 104px;
    line-height: 158px;
    letter-spacing: 2px;
    text-transform: uppercase;
    color: var(--title-face);
    text-shadow: 3px 3px 0 var(--title-edge);
  }
  .cover-title span { display: block; }
  .cover-author {
    position: absolute;
    left: 0;
    right: 0;
    top: 1016px;
    text-align: center;
    font-family: "Cinzel", "Trajan Pro", serif;
    font-weight: 400;
    font-size: 44px;
    line-height: 1;
    letter-spacing: 9px;
    text-transform: uppercase;
    color: var(--author-ink);
  }
</style>
</head>
<body>
  <div class="canvas">
    <div class="book-cover">
      <div class="cover-art" role="img" aria-label="A lone figure in silhouette standing on a dark rocky ledge inside a vast cavern, facing a misty teal glow beyond jagged crystal spires"></div>
      <h1 class="cover-title"><span>Tovald’s</span><span>Hollow</span></h1>
      <p class="cover-author">Author Name</p>
    </div>
  </div>
</body>
</html>
```